Non-Fiction Book: Socio-Political, Spiritual, Self-Transformation

General direction:
Simple yet effective rather than too busy cover. Design to generate emotions of awe and hope - not of fear or futility. To be more on a subtle, elegant level then in readers face. Possible concept to consider: Tasteful indication of persistent presence of God (as light).
Possible ideas:
▫ Taking a blindfold off (preferably group of people) with expression of awe, bewilderment and joy. Their clothing should indicate diverse strata’s of society (professional, racial, cultural, affluence, etc). Not urban environment. Preferably in nature or as per designer creativity.
▫ Concept of duality (light/dark; good/evil; paths (or crossroads) with subtle hint – one branch might be bright; another slight notice of decay. Bright path on the right-hand side). Please don't use road or rail tracks.
▫ Earth from space - play with the light and darkness of the space (this idea is somewhat overused - must be unique to be considered). Interesting images for this concept attached. I don’t have stock image licence though.
▫ Open to artists suggestions.
If you need more clarity on any of the ideas above - please ask.

Thank you for your interest and creative ideas.

Target Market(s)

Who will potentially read this book?
Individuals searching for the answers regarding current world events. Individuals straggling to find a deeper meaning to existence and looking for spiritual direction. Individuals open or willing to consider more metaphysical side of our reality. Audience s/b viewed more from the state of mind then age group, status, sophistication or any other perspective.
What is book about – please read synopsis and extract (files attached) - key points.

Colors

Designer to choose colors to be used in the design.

Requirements
Must have
• A book cover for paperback and ebook.
• Deliverables to include following:
• ▫ Design of front/spine/back for paperback book size: 6 x 9 (Cover template attached),
• ▫ Same cover image for ebook format,
• ▫ Title page using same font(s)/style (black and white, without cover details).
• Number of Pages: 328 (template attached)
• The back cover must include:
• ▫ Synopsis (text is attached),
• ▫ ISBN # and bar code (as per cover template spec) – barcode file will be provided
• ▫ Publisher’s logo (logos attached)
• The Spine must include:
• ▫ Book Title (no subtitle)
• ▫ Authors first name initial and full last name (R. Delmare)
• ▫ Publisher logo
Nice to have
• Tasteful, color, contrasting cover. Objective is to generate curiosity, positive feelings but subtle.
Should not have
• Definitely no promotion of low vibe emotions of fear, destruction, etc.

```html
<!DOCTYPE html>
<html lang="en">
<head>
<meta charset="utf-8">
<title>Edge of Silence — Title Page</title>
<link href="https://fonts.googleapis.com/css2?family=Jost:wght@300;600&family=Cormorant+Garamond:wght@600&display=swap" rel="stylesheet">
<style>
  :root {
    --paper: #ffffff;
    --ink: #111111;
  }
  html, body {
    margin: 0;
    padding: 0;
    overflow: hidden;
    background: var(--paper);
  }
  .title-page {
    position: relative;
    width: 814px;
    height: 1200px;
    background: var(--paper);
    color: var(--ink);
    overflow: hidden;
  }
  .book-title {
    position: absolute;
    left: 0;
    right: 0;
    top: 56px;
    margin: 0;
    text-align: center;
    font-family: "Jost", sans-serif;
    font-weight: 300;
    font-size: 148px;
    line-height: 138px;
    white-space: nowrap;
  }
  .book-title__line {
    display: block;
  }
  .book-title__line--first {
    letter-spacing: 0.05em;
    margin-left: 0.05em;
  }
  .book-title__line--second {
    letter-spacing: 0.17em;
    margin-left: 0.17em;
  }
  .book-subtitle {
    position: absolute;
    left: 0;
    right: 0;
    top: 413px;
    margin: 0;
    text-align: center;
    font-family: "Jost", sans-serif;
    font-weight: 600;
    font-size: 27px;
    line-height: 43px;
    letter-spacing: 0.06em;
    text-transform: uppercase;
    white-space: nowrap;
  }
  .book-author {
    position: absolute;
    left: 0;
    right: 0;
    top: 1091px;
    margin: 0;
    text-align: center;
    font-family: "Cormorant Garamond", serif;
    font-weight: 600;
    font-size: 54px;
    line-height: 1;
    font-variant: small-caps;
    letter-spacing: 0.13em;
    white-space: nowrap;
  }
</style>
</head>
<body>
  <main class="title-page">
    <h1 class="book-title">
      <span class="book-title__line book-title__line--first">EDGE OF</span>
      <span class="book-title__line book-title__line--second">SILENCE</span>
    </h1>
    <p class="book-subtitle">The quiet lie and why we must now<br>reclaim the path of inner awakening</p>
    <p class="book-author">Radovan&nbsp; Delmare</p>
  </main>
</body>
</html>
```